Vintage poster/postcard for 2011 New Years Eve event with theme 'Lumière Volante'

I have had a major change of mind since the last brief due to my original requirements being too specific. I hope this new brief allows more scope for the designers and I am extending the deadline by 7 days.

For the first time my new business 'Tidewell Gala' is planning an exciting, large scale New Years Eve fundraising event in Hobart Tasmania, Australia. The unique and eclectic theme of the party is 'Lumière Volante' (french for contemporary circus). I require a vintage style poster design (similar to a traditional french advertising poster) that can double as a postcard invitation so it must look good on a smaller scale as well.
Updates

Project Deadline Extended
Reason: My original brief was very specific and I now realise very limiting for the designers. I have changed my mind with the look I want for the vintage poster (more along the lines of the traditional french advertising posters of old) and therefore would like to allow designers extra time to submit a design. Thank you. Jill Barrow Tidewell Gala

Target Market(s)

25-50 yr old professionals prepared to pay premium price for a quality, fresh & fun NYE experience while giving to charity.

Industry/Entity Type

Advertising

Requirements
Must have
• - A heading that reads: Tidewell Gala proudly presents
Lumière Volante
- Text that includes: 2011 New Years Eve Extravanaganza Saturday 31st December and find out more at "www.tidewellgala.example
- A strip left blank at the bottom to include my business logo and others sponsors
- Classic french vintage poster design
- - Plenty of colour but not too fluro
- Something that looks good enough to be framed or sent to a friend
Should not have
• - Picture of Eiffel Tower or any other specific French references
- Any animals

```html
<!DOCTYPE html>
<html lang="en">
<head>
<meta charset="utf-8">
<title>Tidewell Gala presents Lumière Volante</title>
<link rel="stylesheet" href="https://fonts.googleapis.com/css2?family=Bebas+Neue&family=Ewert&display=swap">
<style>
  :root {
    --stripe-light: #ffffff;
    --stripe-grey: #f1f1f1;
    --circus-orange: #f05a28;
    --soft-orange: #f5a46e;
    --type-grey: #a7a9ac;
    --ink-grey: #8c8d8f;
    --ribbon-line: #c9c9c9;
  }
  html, body {
    margin: 0;
    padding: 0;
    width: 845px;
    height: 1200px;
    overflow: hidden;
    background: #ffffff;
  }
  .poster {
    position: relative;
    width: 845px;
    height: 1200px;
    overflow: hidden;
    background: repeating-linear-gradient(90deg,
      var(--stripe-light) 0 30px,
      var(--stripe-grey) 30px 60px);
    font-family: "Bebas Neue", "Arial Narrow", sans-serif;
    text-align: center;
  }
  .banner {
    position: absolute;
    left: 158px;
    top: 26px;
    width: 530px;
    height: 190px;
  }
  .banner-name {
    position: absolute;
    left: 0;
    right: 0;
    top: 64px;
    margin: 0;
    font-size: 33px;
    letter-spacing: 1px;
    color: var(--ink-grey);
    font-weight: 400;
  }
  .presents {
    position: absolute;
    left: 0;
    right: 0;
    top: 160px;
    margin: 0;
    font-size: 16px;
    letter-spacing: 0.5px;
    color: var(--type-grey);
  }
  .dot-rule {
    position: absolute;
    left: 50px;
    width: 746px;
    height: 8px;
    background: radial-gradient(circle, var(--soft-orange) 3.4px, transparent 3.9px) 0 0 / 20.7px 8px repeat-x;
  }
  .dot-rule.top { top: 224px; }
  .dot-rule.middle { top: 567px; }
  .dot-rule.bottom { top: 988px; }
  .show-title {
    position: absolute;
    left: 0;
    right: 0;
    top: 248px;
    margin: 0;
    font-family: "Ewert", "Rye", serif;
    font-weight: 400;
    font-size: 128px;
    line-height: 140px;
    letter-spacing: 2px;
    color: var(--circus-orange);
    text-shadow: 4px 4px 0 #d8461a;
  }
  .show-title span { display: block; }
  .occasion {
    position: absolute;
    left: 0;
    right: 0;
    top: 608px;
    margin: 0;
    font-size: 58px;
    line-height: 58px;
    color: var(--type-grey);
    font-weight: 400;
  }
  .extravaganza {
    position: absolute;
    left: 0;
    right: 0;
    top: 678px;
    margin: 0;
    font-family: "Ewert", "Rye", serif;
    font-size: 66px;
    line-height: 84px;
    letter-spacing: 1px;
    color: var(--type-grey);
    font-weight: 400;
  }
  .line-rule {
    position: absolute;
    left: 36px;
    width: 770px;
    height: 4px;
    background: var(--soft-orange);
  }
  .line-rule.upper { top: 782px; }
  .line-rule.lower { top: 877px; }
  .event-date {
    position: absolute;
    left: 0;
    right: 0;
    top: 803px;
    margin: 0;
    font-size: 56px;
    line-height: 56px;
    letter-spacing: 0.5px;
    color: var(--type-grey);
  }
  .more-info {
    position: absolute;
    left: 0;
    right: 0;
    top: 898px;
    margin: 0;
    font-size: 20px;
    color: var(--ink-grey);
  }
  .website {
    position: absolute;
    left: 0;
    right: 0;
    top: 928px;
    margin: 0;
    font-size: 36px;
    letter-spacing: 1.5px;
    color: var(--ink-grey);
  }
</style>
</head>
<body>
  <main class="poster">
    <svg class="banner" viewBox="0 0 530 190" aria-hidden="true">
      <path d="M70 62 L8 70 L40 108 L2 152 L100 128 Z" fill="#ffffff" stroke="var(--ribbon-line)" stroke-width="3" stroke-linejoin="round"/>
      <path d="M460 62 L522 70 L490 108 L528 152 L430 128 Z" fill="#ffffff" stroke="var(--ribbon-line)" stroke-width="3" stroke-linejoin="round"/>
      <path d="M70 62 L100 128 L112 110 Z" fill="#e6e6e6" stroke="var(--ribbon-line)" stroke-width="3" stroke-linejoin="round"/>
      <path d="M460 62 L430 128 L418 110 Z" fill="#e6e6e6" stroke="var(--ribbon-line)" stroke-width="3" stroke-linejoin="round"/>
      <path d="M70 62 Q265 5 460 62 L418 110 Q265 62 112 110 Z" fill="#ffffff" stroke="var(--ribbon-line)" stroke-width="3" stroke-linejoin="round"/>
    </svg>
    <p class="banner-name">Tidewell Gala</p>
    <p class="presents">Proudly presents</p>

    <div class="dot-rule top"></div>
    <h1 class="show-title"><span>LUMIÈRE</span><span>VOLANTE</span></h1>
    <div class="dot-rule middle"></div>

    <h2 class="occasion">New Years Eve</h2>
    <p class="extravaganza">EXTRAVAGANZA</p>

    <div class="line-rule upper"></div>
    <p class="event-date">Saturday 31st December 2011</p>
    <div class="line-rule lower"></div>

    <p class="more-info">Find out more at</p>
    <p class="website">www.tidewellgala.example</p>
    <div class="dot-rule bottom"></div>
  </main>
</body>
</html>
```